Buch-/E-Book-Cover für ein Lernbuch
Vielen Dank für die ausgezeichnete Arbeit! Gerne wieder! vorlage7
Zielgruppe
Ich biete Lerncoachings und Prüfungscoaching für Schüler und Studenten an.
Meine Zielgruppe sind Schüler von 12-18 Jahren und Eltern und erziehungsberechtigte Personen.
Aufgabenstellung
Ich benötige ein ansprechendes Buch-Cover. Das Format für das Buch ist 15,24 x 22,86 cm (6' x 9').
Mein Buch Cover soll sich aber deutlich von den anderen Büchern abheben und Jugendliche (keine Kinder) ansprechen.
Wichtig ist mir auch einen Wiedererkennungswert vom Buch-Cover zu haben.
Bitte um ein ansprechendes Bild, denn ich möchte mich deutlich von meiner Konkurrenz abheben.
Autoren: Ursula Brenning und Gerda Brenning
Titel: Der Kompass für den sicheren Weg durch den Alltag
Untertitel: Kluge Wege durch jede Woche im Jahr
Buchrücken
Lernen ist nicht gleich Lernen. Was ist Lernen und welche Lernmethoden sind erfolgreich? Das sind die Fragen, die dieses Buch beantwortet.
Warum ist es wichtig zu lernen, wie man lernt? Lernen ist ein wichtiger Prozess für Kinder und Schüler. Sie verbringen viel Zeit damit, neues Wissen aufzunehmen, und es hört nie auf. Denn wir lernen fürs Leben – lebenslanges Lernen. Wir lernen laufen, wir lernen sprechen, wir lernen rechnen und so weiter. Lernen begleitet uns ein Leben lang. Das Auswendiglernen von neuem Wissen ist sehr wichtig, und die richtigen Lernmethoden sind dabei sehr hilfreich. Die notwendige Struktur kann durch entsprechende Lernpläne erreicht werden, die unter Berücksichtigung von Lernorganisation und Zeitmanagement erstellt werden.
Um schnell und erfolgreich zu lernen, braucht es die richtigen Lernmethoden.
Eines ist dabei immer wichtig: Lernen darf und soll Spaß machen und Lernen kann stressfrei sein. Jeder kann lernen zu lernen. In diesem Buch zeigen wir, wie unterschiedliche Lerntypen und unterschiedliche Lernmethoden zum gewünschten Schulerfolg führen.
Mein Name ist Ursula Brenning und gemeinsam mit meiner Mutter Gerda Brenning haben wir dieses Buch geschrieben. Sie profitieren in diesem Buch von der langjährigen Erfahrung meiner Mutter Gerda Brenning, die über 40 Jahre als Lehrerin in einer Mittelschule tätig war, u..

```html
<!DOCTYPE html>
<html lang="de">
<head>
<meta charset="utf-8">
<title>Buchrücken – Klappentext</title>
<link href="https://fonts.googleapis.com/css2?family=Bitter:wght@600&display=swap" rel="stylesheet">
<style>
  :root {
    --cover-teal: #02969c;
    --text-white: #ffffff;
  }
  html, body {
    margin: 0;
    padding: 0;
    overflow: hidden;
  }
  .back-cover {
    width: 752px;
    height: 1200px;
    background: var(--cover-teal);
    box-sizing: border-box;
    padding: 77px 30px 0 35px;
    overflow: hidden;
  }
  .blurb p {
    margin: 0 0 24.5px 0;
    font-family: "Bitter", Georgia, serif;
    font-weight: 600;
    font-size: 19px;
    line-height: 24.5px;
    letter-spacing: 0.2em;
    text-transform: uppercase;
    color: var(--text-white);
  }
</style>
</head>
<body>
  <main class="back-cover">
    <section class="blurb">
      <p>Lernen ist nicht gleich Lernen. Was ist Lernen und welche Lernmethoden sind erfolgreich? Das sind die Fragen, die dieses Buch beantwortet.</p>
      <p>Warum ist es wichtig zu lernen, wie man lernt? Lernen ist ein wichtiger Prozess für Kinder und Schüler. Sie verbringen viel Zeit damit, neues Wissen aufzunehmen, und es hört nie auf. Denn wir lernen fürs Leben – lebenslanges Lernen. Wir lernen laufen, wir lernen sprechen, wir lernen rechnen und so weiter. Lernen begleitet uns ein Leben lang.</p>
      <p>Das Auswendiglernen von neuem Wissen ist sehr wichtig, und die richtigen Lernmethoden sind dabei sehr hilfreich. Die notwendige Struktur kann durch entsprechende Lernpläne erreicht werden, die unter Berücksichtigung von Lernorganisation und Zeitmanagement erstellt werden.</p>
      <p>Um schnell und erfolgreich zu lernen, braucht es die richtigen Lernmethoden. Eines ist dabei immer wichtig: Lernen darf und soll Spaß machen und Lernen kann stressfrei sein. Jeder kann lernen zu lernen. In diesem Buch zeigen wir, wie unterschiedliche Lerntypen und unterschiedliche Lernmethoden zum gewünschten Schulerfolg führen.</p>
      <p>Mein Name ist Ursula Brenning und gemeinsam mit meiner Mutter Gerda Brenning haben wir dieses Buch geschrieben. Sie profitieren in diesem Buch von der langjährigen Erfahrung meiner Mutter Gerda Brenning, die über 40 Jahre als Lehrerin in einer Mittelschule tätig war, und von meinen Erfahrungen.</p>
    </section>
  </main>
</body>
</html>
```